Orbell Consulting- executive coaching business

looking for business card design for a newly started coaching business.
specialising in Exective coaching, Leadership, NLP and Motivation.
Looking for a simple, classy design using the existing logo attached and colour themes that complement the logo.
No red or orange in the business card design please.

Target Market(s)

Defence and Veteran community

Industry/Entity Type

Life Coaching

Contact Information for Business Card

looking for business cards for newly started coaching business.
specialising in Exective Coaching, Leadership, NLP and Motivation

Font styles to use
Serif
Script

Colors
0556a4
3176b5
86cfc6
33b8a4

Requirements
Must have
• Logo
• Email address- Jess@orbellconsulting.com.au
• Contact number
• Services provided - Executive Coaching, Leadership, NLP and Motivational Mapping.
Nice to have
• Same colours as logo
Should not have
• Red or orange

```html
<!DOCTYPE html>
<html lang="en">
<head>
<meta charset="utf-8">
<title>Orbell Consulting – Business Cards</title>
<link href="https://fonts.googleapis.com/css2?family=Roboto+Slab:wght@400;500;700;800&display=swap" rel="stylesheet">
<style>
  :root {
    --bg: #2b2b2b;
    --card: #050505;
    --blue: #0556a4;
    --blue-soft: #3176b5;
    --green: #33b8a4;
    --white: #ffffff;
    --grey: #9a9a9a;
    --text: #e8e8e8;
    --faint: #1a1a1a;
  }
  * { margin: 0; padding: 0; box-sizing: border-box; }
  html, body {
    width: 1200px; height: 900px; overflow: hidden;
    background: var(--bg);
    font-family: "Roboto Slab", serif;
  }
  .canvas { position: relative; width: 1200px; height: 900px; }
  .card {
    position: absolute;
    width: 665px; height: 380px;
    background: var(--card);
    border-radius: 22px;
    overflow: hidden;
    box-shadow: 0 14px 30px rgba(0,0,0,.5);
  }
  .card--front { left: 110px; top: 45px; }
  .card--back { left: 425px; top: 475px; }

  .stripe {
    position: absolute; left: 0; right: 0; bottom: 0; height: 12px;
    display: flex;
  }
  .stripe__blue { flex: 0 0 40%; background: var(--blue-soft); }
  .stripe__white { flex: 0 0 32%; background: var(--white); }
  .stripe__green { flex: 1; background: var(--green); }

  /* front */
  .brand-mark {
    position: absolute; left: 70px; top: 95px;
    width: 180px; height: 180px;
    display: flex; align-items: center; justify-content: center;
  }
  .brand-mark__ring {
    position: absolute; inset: 0;
    border: 4px solid var(--grey); border-radius: 50%;
  }
  .brand-mark__name {
    position: relative; color: var(--text);
    font-weight: 500; font-size: 21px; text-align: center; line-height: 1.25;
  }
  .services {
    position: absolute; left: 345px; top: 105px;
    list-style: none; color: var(--text);
    font-size: 15px; line-height: 1.45;
  }
  .services li { position: relative; padding-left: 20px; }
  .services li::before {
    content: ""; position: absolute; left: 0; top: 7px;
    width: 8px; height: 8px; border-radius: 50%; background: var(--blue-soft);
  }
  .faint-ring {
    position: absolute; right: -50px; top: 90px;
    width: 260px; height: 260px;
    border: 5px solid var(--faint); border-radius: 50%;
  }

  /* back */
  .wordmark {
    position: absolute; left: 50px; top: 120px; width: 240px;
    display: flex; flex-direction: column; align-items: center; gap: 14px;
  }
  .wordmark__dot {
    width: 62px; height: 62px; border: 3px solid var(--grey); border-radius: 50%;
  }
  .wordmark__name {
    color: var(--blue-soft); font-weight: 500; font-size: 25px; white-space: nowrap;
  }
  .divider {
    position: absolute; left: 322px; top: 95px; width: 2px; height: 120px;
    background: var(--grey);
  }
  .contact { position: absolute; left: 350px; top: 95px; color: var(--text); }
  .contact__name { font-weight: 800; font-size: 28px; color: var(--white); line-height: 1.1; }
  .contact__role { font-size: 14px; color: var(--green); letter-spacing: 1px; margin-bottom: 14px; }
  .contact__line { display: flex; align-items: center; gap: 9px; font-size: 14px; line-height: 1.7; }
  .contact__line svg { width: 12px; height: 12px; flex: none; }
</style>
</head>
<body>
<div class="canvas">

  <section class="card card--front">
    <div class="brand-mark">
      <div class="brand-mark__ring"></div>
      <div class="brand-mark__name">Orbell<br>Consulting</div>
    </div>
    <ul class="services">
      <li>Executive Coaching</li>
      <li>Leadership</li>
      <li>NLP</li>
      <li>Motivational Mapping</li>
    </ul>
    <div class="faint-ring"></div>
    <div class="stripe"><span class="stripe__blue"></span><span class="stripe__white"></span><span class="stripe__green"></span></div>
  </section>

  <section class="card card--back">
    <div class="wordmark">
      <div class="wordmark__dot"></div>
      <div class="wordmark__name">Orbell Consulting</div>
    </div>
    <div class="divider"></div>
    <div class="contact">
      <div class="contact__name">Liam Carter</div>
      <div class="contact__role">DIRECTOR</div>
      <div class="contact__line">
        <svg viewBox="0 0 24 24" aria-hidden="true"><path fill="#33b8a4" d="M6.6 10.8a15.1 15.1 0 0 0 6.6 6.6l2.2-2.2a1 1 0 0 1 1-.25 11.4 11.4 0 0 0 3.6.57 1 1 0 0 1 1 1V20a1 1 0 0 1-1 1A17 17 0 0 1 3 4a1 1 0 0 1 1-1h3.5a1 1 0 0 1 1 1c0 1.25.2 2.45.57 3.57a1 1 0 0 1-.25 1z"/></svg>
        <span>123 456 7890</span>
      </div>
      <div class="contact__line">
        <svg viewBox="0 0 24 24" aria-hidden="true"><rect x="2" y="5" width="20" height="14" rx="2" fill="none" stroke="#33b8a4" stroke-width="2.2"/><path d="M3 6l9 7 9-7" fill="none" stroke="#33b8a4" stroke-width="2.2"/></svg>
        <span>Jess@orbellconsulting.com.au</span>
      </div>
      <div class="contact__line">
        <svg viewBox="0 0 24 24" aria-hidden="true"><circle cx="12" cy="12" r="9" fill="none" stroke="#33b8a4" stroke-width="2.2"/><path d="M3 12h18M12 3c3 3 3 15 0 18M12 3c-3 3-3 15 0 18" fill="none" stroke="#33b8a4" stroke-width="1.8"/></svg>
        <span>www.orbellconsulting.com.au</span>
      </div>
    </div>
    <div class="stripe"><span class="stripe__blue"></span><span class="stripe__white"></span><span class="stripe__green"></span></div>
  </section>

</div>
</body>
</html>
```